Tallowmere Office Partners needs a new interactive and interesting website

We need an interesting, professional, modern and functional company website for Tallowmere Office Partners - a young IT Services company based out of Chennai, India.

Tallowmere Office Partners is a fully owned subsidiary of Hollin Cellarworks, one of the world's leading direct to consumer wine merchant.

We already have a registered company logo which must feature in the website.

We conceive, design, develop, test, implement and support IT solutions across the entire Hollin Cellarworks IT landscape. For ex : We currently run about 25 e-commerce websites for Hollin Cellarworks on KVM and Dot Net.

We would like to see our corporate colors used in the website. (Burgundy wine and wine green - source: www.tallowmereop.example)

We are looking at this website to communicate a fun, friendly and professionally managed company - reaching out to career seekers, prospective customers and general public.

For reference - The company name 'Tallowmere' is an inspiration from the Hollin Cellarworks lineage.

The second image with the world map is stickered on our main entrance to the office, I am not sure where this can be used -just putting it out there..
Updates

Please note that there are only a few more days to submit designs for this contest  !

I would appreciate if you can help posting your designs in time for our review and consideration.

Thanks.

Reason: Thanks for your inputs. We have a number of designers and a lot to digest and work with in the past few days. There has been a rush of new designs in the last few days Hence we will require more time to process these and make our decision. Hence i am requesting the contest to be open for more days. Regards, Suresh

Target Market(s)

Prospective job seekers who want to know more about the company and also wish to apply for a job vacancy
People wanting to know more about the company in general and our progress
People who want to see what we offer and how we can help them too - prospective customers
Companies that are interested in our IT Captive journey and are looking for a business opportunity

Industry/Entity Type

E-Commerce

Requirements
Must have
• Log In/ Register facility acting as a Single Sign on for Intranet (Employees)

Facility to post job vacancies (with an expiry date) and enable people to apply for a role and upload their CV/Resume.

Facility to Review Job applications

Facility for website visitors to contact Tallowmere Office Partners via an online 'Contact Us' form with a split of job seekers and business opportunities

Gallery facility to upload pictures regarding company events
Nice to have
• Less Cluttered and contemporary design
Some Wine/Vineyard inspirations will be good but not too much, the company is an IT services company

```html
<!DOCTYPE html>
<html lang="en">
<head>
<meta charset="utf-8">
<title>Tallowmere Office Partners</title>
<link href="https://fonts.googleapis.com/css2?family=Arimo:wght@400;700&display=swap" rel="stylesheet">
<style>
:root{
  --wine:#8e0a47;
  --wine-deep:#7a0a3f;
  --wine-light:#a0165a;
  --white:#ffffff;
  --ink:#555555;
  --ink-soft:#777777;
  --link-blue:#1e8ee0;
  --footer:#333333;
  --rule:#dddddd;
}
*{margin:0;padding:0;box-sizing:border-box}
html,body{width:1200px;height:1000px;overflow:hidden}
body{position:relative;font-family:"Arimo",Arial,sans-serif;background:var(--wine);color:var(--ink)}
.abs{position:absolute}
.topbar{left:0;top:0;width:1200px;height:37px;background:var(--wine-deep)}
.toplinks{left:441px;top:0;width:581px;height:37px;background:var(--white);font-size:9px;color:#888;text-align:right;padding:7px 18px 0 0}
.headband{left:0;top:37px;width:1200px;height:42px;background:var(--white)}
.brand{display:flex;align-items:center;gap:6px;color:var(--wine);font-weight:700}
.brand .dot{width:12px;height:12px;border-radius:50%;background:currentColor}
.head-brand{left:218px;top:46px;font-size:20px}
.nav{left:441px;top:37px;width:581px;height:42px;background:var(--wine-deep);display:flex;align-items:center}
.nav a{color:var(--white);text-decoration:none;font-size:11px;font-weight:700;position:absolute;top:16px}
.stage{left:0;top:79px;width:1200px;height:806px;background:linear-gradient(160deg,#a0145a 0%,#8e0a47 40%,#9c1556 70%,#880943 100%)}
.hero-side{left:192px;top:79px;width:249px;height:282px;background:var(--wine)}
.hero-brand{left:218px;top:178px;color:var(--white);font-weight:700;font-size:22px;line-height:1.05}
.hero-brand .sub{display:block;font-weight:400;font-size:15px;padding-left:18px}
.hero-text{left:218px;top:242px;width:205px;color:var(--white);font-size:12.5px;line-height:17px}
.hero-top{left:441px;top:79px;width:581px;height:119px;background:var(--white)}
.hero-photo{left:441px;top:198px;width:581px;height:163px;background:linear-gradient(90deg,#f4f4f4 0%,#e8e8e8 45%,#c8b3a5 75%,#e6e6e6 100%)}
.caption{left:441px;top:291px;width:301px;height:70px;background:rgba(110,110,110,.85);color:var(--white);padding:4px 6px}
.caption h2{font-weight:400;font-size:16px;letter-spacing:.5px}
.caption p{font-size:7.5px;line-height:10px;margin-top:8px}
.pager{left:892px;top:339px;display:flex;gap:4px}
.pager span{width:11px;height:11px;background:var(--wine)}
.pager span:first-child{background:#222}
.content{left:192px;top:361px;width:830px;height:544px;background:var(--white)}
.col-title{font-size:13px;color:var(--wine);font-weight:400}
.readmore{font-size:8.5px;color:#999;font-weight:700;text-decoration:underline}
.welcome{left:218px;top:396px;width:250px}
.welcome h3{font-size:10px;font-weight:700;color:var(--ink);margin-top:28px}
.welcome-img{width:249px;height:124px;margin-top:21px;background:linear-gradient(160deg,#ffffff 0%,#cfe3f4 45%,#3a8fd6 100%)}
.welcome p{font-size:8.5px;line-height:17px;margin-top:14px;color:var(--ink-soft)}
.welcome .readmore{display:block;margin-top:8px}
.jobs{left:486px;top:396px;width:240px}
.job{margin-top:28px}
.job+.job{margin-top:26px}
.job .date{font-size:8.5px;font-style:italic;color:var(--ink-soft)}
.job h4{font-size:9px;font-weight:700;margin-top:15px}
.job h4.live{color:var(--link-blue)}
.job p{font-size:8.5px;margin-top:4px;color:var(--ink-soft)}
.job .readmore{display:block;margin-top:8px}
.services{left:755px;top:361px;width:248px;height:391px;background:var(--wine);color:var(--white);padding:35px 14px}
.services .col-title{color:var(--white)}
.services ul{list-style:none;margin-top:26px}
.services li{font-size:9.5px;font-weight:700;line-height:17px}
.services p{font-size:8.5px;line-height:17.2px;margin-top:28px}
.rule{left:218px;top:773px;width:785px;height:1px;background:var(--rule)}
.clients{left:218px;top:812px;width:785px;height:40px;display:flex;align-items:center;justify-content:space-between}
.clients .arrow{font-size:20px;color:#aaa}
.clients .client{font-size:12px;font-weight:700;color:var(--wine);text-align:center;width:110px}
.footer{left:0;top:885px;width:1200px;height:115px;background:var(--footer)}
.foot-brand{left:192px;top:934px;color:var(--white);font-weight:700;font-size:18px;line-height:1}
.foot-brand .sub{display:block;font-weight:400;font-size:12px;padding-left:18px}
.foot-links{left:340px;top:940px;color:var(--white);font-size:8.5px}
.foot-links p+p{margin-top:10px}
.social{top:950px;display:flex;align-items:flex-end;gap:4px;color:var(--white);font-size:6px}
.social .dot{width:14px;height:14px;border-radius:50%;background:var(--white)}
</style>
</head>
<body>
<div class="abs topbar"></div>
<div class="abs toplinks">Current Opportunity &nbsp;|&nbsp; Contact Us</div>
<div class="abs headband"></div>
<div class="abs brand head-brand"><span class="dot"></span>Tallowmere</div>
<nav class="abs nav">
  <a style="left:46px">Home</a><a style="left:122px">About us</a><a style="left:231px">Clients</a>
  <a style="left:302px">Services</a><a style="left:385px">Careers</a><a style="left:488px">Contact us</a>
</nav>

<div class="abs stage"></div>
<div class="abs hero-side"></div>
<div class="abs brand hero-brand"><span><span class="dot" style="display:inline-block;margin-right:6px"></span>Tallowmere<span class="sub">Office Partners</span></span></div>
<p class="abs hero-text">Lorem ipsum dolor sit amet, consectetur adipisicing elit, sed do eiusmod tempor incididunt ut labore et dolore magna aliqua.</p>
<div class="abs hero-top"></div>
<div class="abs hero-photo" role="img" aria-label="Photo of a man sketching a growth chart with a marker"></div>
<div class="abs caption">
  <h2>Be equipped for the future...</h2>
  <p>Plan your moves with a broader, deeper and in-depth<br>process understanding and tap the unseen umpteen opportunities.</p>
</div>
<div class="abs pager"><span></span><span></span><span></span><span></span></div>

<main class="abs content"></main>
<section class="abs welcome">
  <h2 class="col-title">Welcome</h2>
  <h3>Delivering IT Excellence</h3>
  <div class="welcome-img" role="img" aria-label="Illustration of a web address bar with a mouse cursor"></div>
  <p>Welcome to Tallowmere Office Partners, an emerging provider of global IT consulting and software services. We are part of the Hollin Cellarworks group, a family run business and the world's largest multi-channel home delivery wine merchant operating in the UK, USA, Australia, Germany, Hong Kong, Poland and Switzerland.</p>
  <span class="readmore">read more &gt;&gt;</span>
</section>
<section class="abs jobs">
  <h2 class="col-title">Latest opportunities</h2>
  <div class="job">
    <div class="date">26/11/2013</div>
    <h4 class="live">Software Developers/Programmer Analysts - QX</h4>
    <p>We are looking for a QX Software Developer to join</p>
    <span class="readmore">read more &gt;&gt;</span>
  </div>
  <div class="job">
    <div class="date">26/11/2013</div>
    <h4>Software Developers/Programmer Analysts - KVM</h4>
    <p>We are looking for a KVM Software Developer to join</p>
    <span class="readmore">read more &gt;&gt;</span>
  </div>
</section>
<section class="abs services">
  <h2 class="col-title">Services</h2>
  <ul>
    <li>Packaged Applications</li><li>Enterprise Application Integration</li>
    <li>Digital Commerce</li><li>Application Development &amp; Maintenance</li>
  </ul>
  <p>The services we provide enable the businesses we support to efficiently manage key functions, including order management (encompassing e-commerce websites, inbound and outbound call centre operations), order fulfilment, procurement, planning &amp; forecasting, warehouse management operations, financial management, global compliance and risk</p>
</section>
<div class="abs rule"></div>
<div class="abs clients">
  <span class="arrow">&#x2039;</span>
  <span class="client">Brackenfold Wine</span>
  <span class="client">Lumen Wines</span>
  <span class="client">Daily Ledger Wine</span>
  <span class="client">Corlett Fine Wine</span>
  <span class="client">Weekend Courier Wine Club</span>
  <span class="client">Hollin Cellarworks</span>
  <span class="arrow">&#x203A;</span>
</div>

<footer class="abs footer"></footer>
<div class="abs brand foot-brand" style="color:var(--white)"><span><span class="dot" style="display:inline-block;margin-right:6px"></span>Tallowmere<span class="sub">Office Partners</span></span></div>
<div class="abs foot-links">
  <p>Home | About us | Clients | Services | Careers | Contact us</p>
  <p>Copyright Tallowmere Office Partners Private Limited. 2014</p>
</div>
<div class="abs social" style="left:920px"><span class="dot"></span>Friendwall</div>
<div class="abs social" style="left:982px"><span class="dot"></span>Chirpline</div>
</body>
</html>
```